brindlewood carpentry business card 2.0

id like to get some extra info added to my current business card ,but i am also open to a new design as well ,id like it to be a clean professional look
i have attached the original card files, i have also attached the ridgemark guild logo and licensed builder logo that id like to add to all the current info on the old card
also the color green is important as seen in the company logo

Industry/Entity Type

Carpentry

Colors
9bcb3c

```html
<!DOCTYPE html>
<html lang="en">
<head>
<meta charset="utf-8">
<title>Brindlewood Carpentry – Business Card</title>
<link href="https://fonts.googleapis.com/css2?family=Montserrat:wght@500;700&family=Arimo:wght@400&display=swap" rel="stylesheet">
<style>
  :root {
    --backdrop: #2b2b2c;
    --card: #1f2021;
    --card-pattern: #28292a;
    --brand-green: #9bcb3c;
    --ink-white: #ffffff;
    --ink-soft: #e6e6e6;
    --rule: #6b6b6b;
    --badge-blue: #2a3d8f;
    --badge-pale: #eef0e6;
  }
  html, body {
    margin: 0;
    padding: 0;
    width: 1200px;
    height: 1108px;
    overflow: hidden;
    background: var(--backdrop);
  }
  .canvas {
    position: relative;
    width: 1200px;
    height: 1108px;
  }
  .card {
    position: absolute;
    top: 204px;
    width: 420px;
    height: 700px;
    background: var(--card);
    border-radius: 22px;
    overflow: hidden;
  }
  .card--front { left: 150px; }
  .card--back { left: 630px; }

  .wordmark {
    position: absolute;
    left: 0;
    right: 0;
    text-align: center;
    font-family: "Montserrat", sans-serif;
    font-weight: 500;
    color: var(--ink-white);
    line-height: 1.15;
  }
  .wordmark__name {
    display: inline-flex;
    align-items: center;
    gap: 12px;
    font-size: 40px;
    letter-spacing: 1px;
  }
  .wordmark__square {
    width: 14px;
    height: 14px;
    background: var(--brand-green);
  }
  .wordmark__trade {
    display: block;
    font-size: 24px;
    letter-spacing: 3px;
  }
  .card--front .wordmark { top: 150px; }
  .card--back .wordmark { top: 378px; }

  .contact {
    position: absolute;
    left: 0;
    right: 0;
    top: 420px;
    text-align: center;
    font-family: "Arimo", sans-serif;
    color: var(--ink-white);
  }
  .contact__name {
    font-family: "Montserrat", sans-serif;
    font-weight: 700;
    font-size: 27px;
    color: var(--brand-green);
    margin: 0;
    letter-spacing: 0.5px;
  }
  .contact__role {
    font-size: 18px;
    margin: 6px 0 0;
  }
  .contact__icons {
    display: flex;
    align-items: center;
    justify-content: center;
    gap: 8px;
    margin: 22px auto 14px;
    width: 320px;
  }
  .contact__rule {
    flex: 1;
    height: 1px;
    background: var(--rule);
  }
  .contact__icon {
    width: 28px;
    height: 28px;
    background: var(--brand-green);
    border-radius: 3px;
    display: flex;
    align-items: center;
    justify-content: center;
  }
  .contact__line {
    font-size: 19px;
    margin: 4px 0 0;
    color: var(--ink-soft);
  }

  .back-pattern {
    position: absolute;
    left: 0;
    top: 0;
    width: 420px;
    height: 360px;
    background: linear-gradient(180deg, var(--card-pattern) 0%, var(--card) 100%);
  }
  .badges {
    position: absolute;
    left: 40px;
    top: 540px;
    display: flex;
    align-items: center;
    gap: 22px;
  }
  .badge--square {
    width: 82px;
    height: 104px;
    background: var(--badge-blue);
    border: 4px solid var(--ink-white);
    box-sizing: border-box;
  }
  .badge--round {
    width: 100px;
    height: 100px;
    border-radius: 50%;
    background: var(--badge-pale);
    border: 5px solid var(--brand-green);
    box-sizing: border-box;
  }
</style>
</head>
<body>
<main class="canvas">

  <section class="card card--front" aria-label="Card front">
    <div class="wordmark">
      <span class="wordmark__name"><span class="wordmark__square"></span>BRINDLEWOOD</span>
      <span class="wordmark__trade">CARPENTRY</span>
    </div>

    <div class="contact">
      <p class="contact__name">MARTIN HALE</p>
      <p class="contact__role">Director / Brindlewood Carpentry Ltd</p>
      <div class="contact__icons">
        <span class="contact__rule"></span>
        <span class="contact__icon">
          <svg width="18" height="18" viewBox="0 0 24 24" aria-label="Phone"><path d="M6.6 10.8a15 15 0 0 0 6.6 6.6l2.2-2.2c.3-.3.7-.4 1-.2 1.1.4 2.3.6 3.6.6.6 0 1 .4 1 1V20c0 .6-.4 1-1 1A17 17 0 0 1 3 4c0-.6.4-1 1-1h3.5c.6 0 1 .4 1 1 0 1.3.2 2.5.6 3.6.1.3 0 .7-.2 1z" fill="#1f2021"/></svg>
        </span>
        <span class="contact__icon">
          <svg width="18" height="18" viewBox="0 0 24 24" aria-label="Email"><rect x="3" y="6" width="18" height="12" fill="none" stroke="#1f2021" stroke-width="2"/><path d="M3 6l9 7 9-7" fill="none" stroke="#1f2021" stroke-width="2"/></svg>
        </span>
        <span class="contact__icon">
          <svg width="18" height="18" viewBox="0 0 24 24" aria-label="Website"><circle cx="12" cy="12" r="9" fill="none" stroke="#1f2021" stroke-width="2"/><path d="M3 12h18M12 3c3 3 3 15 0 18M12 3c-3 3-3 15 0 18" fill="none" stroke="#1f2021" stroke-width="1.6"/></svg>
        </span>
        <span class="contact__rule"></span>
      </div>
      <p class="contact__line">02105550148</p>
      <p class="contact__line">martin@brindlewoodcarpentry.co.nz</p>
      <p class="contact__line">www.brindlewoodcarpentry.co.nz</p>
    </div>
  </section>

  <section class="card card--back" aria-label="Card back">
    <div class="back-pattern" role="img" aria-label="Faint repeating brand pattern"></div>
    <div class="wordmark">
      <span class="wordmark__name"><span class="wordmark__square"></span>BRINDLEWOOD</span>
      <span class="wordmark__trade">CARPENTRY</span>
    </div>
    <div class="badges">
      <div class="badge--square" role="img" aria-label="Ridgemark Guild membership badge"></div>
      <div class="badge--round" role="img" aria-label="Licensed builder certification badge"></div>
    </div>
  </section>

</main>
</body>
</html>
```